Autora necesita un cover para su nuevo libro acerca de empoderamiento femenino*

Diseño de cover para libro digital sobre empoderamiento femenino.

El título del libro es: "Las 7 Raíces del Alma Luminosa"
Subtítulo: Descubre tu fuerza interior, tu calma y tu propósito

Autora: Rosaura Beltrán

Target Market(s)

Mujeres

Font styles to use
Sans Serif

Requirements
Must have
• El título del libro es: "Las 7 Raíces del Alma Luminosa"

Autora: Rosaura Beltrán
Should not have
• Sin imágenes

```html
<!DOCTYPE html>
<html lang="es">
<head>
<meta charset="UTF-8">
<title>Las 7 Raíces del Alma Luminosa — Rosaura Beltrán</title>
<link rel="stylesheet" href="https://fonts.googleapis.com/css2?family=Comic+Neue:wght@700&family=Tinos:wght@700&family=Poppins:wght@600&display=swap">
<style>
  :root {
    --page-bg: #e6e6e6;
    --magenta-deep: #a81c78;
    --magenta: #c2408f;
    --pink-soft: #dc98bd;
    --glow: #f6e6d8;
    --night: #060204;
    --title-pink: #b8307f;
    --subtitle-white: #ffffff;
  }
  * { margin: 0; padding: 0; box-sizing: border-box; }
  html, body {
    width: 1200px;
    height: 800px;
    overflow: hidden;
    background: var(--page-bg);
  }
  .canvas {
    width: 1200px;
    height: 800px;
    display: flex;
    align-items: center;
    justify-content: center;
  }
  .book-cover {
    position: relative;
    width: 458px;
    height: 700px;
    background: var(--night);
    overflow: hidden;
  }
  .cover-art {
    position: absolute;
    inset: 0;
    background:
      radial-gradient(ellipse 45% 26% at 55% 40%, var(--glow) 0%, var(--pink-soft) 40%, transparent 80%),
      linear-gradient(to bottom, var(--magenta-deep) 0%, var(--magenta) 22%, var(--pink-soft) 36%, var(--magenta) 42%, var(--night) 47%, var(--night) 100%);
  }
  .cover-text {
    position: absolute;
    inset: 0;
    text-align: center;
  }
  .book-title {
    position: absolute;
    top: 312px;
    left: 0;
    right: 0;
    font-family: "Comic Neue", "Comic Sans MS", cursive;
    font-weight: 700;
    font-size: 56px;
    line-height: 58px;
    color: var(--title-pink);
    text-transform: uppercase;
    letter-spacing: 0.5px;
  }
  .book-subtitle {
    position: absolute;
    top: 561px;
    left: 0;
    right: 0;
    font-family: "Tinos", "Times New Roman", serif;
    font-weight: 700;
    font-size: 23px;
    line-height: 31px;
    color: var(--subtitle-white);
    text-transform: uppercase;
  }
  .book-author {
    position: absolute;
    top: 652px;
    left: 0;
    right: 0;
    font-family: "Poppins", Arial, sans-serif;
    font-weight: 600;
    font-size: 21px;
    letter-spacing: 4px;
    color: var(--title-pink);
  }
</style>
</head>
<body>
  <main class="canvas">
    <section class="book-cover">
      <div class="cover-art" role="img" aria-label="Ilustración: silueta de una mujer heroína con capa sobre la cima de una montaña oscura, ante rayos de luz rosa y una ciudad al fondo"></div>
      <div class="cover-text">
        <h1 class="book-title">Las 7<br>Raíces<br>del Alma<br>Luminosa</h1>
        <p class="book-subtitle">Descubre tu fuerza interior,<br>tu calma y tu propósito</p>
        <p class="book-author">Rosaura Beltrán</p>
      </div>
    </section>
  </main>
</body>
</html>
```